Recruiting ad for Caregivers and Nurses

We need a few amazing, fun, catchy, creative recruiting ads for Caregivers and Nurses to care for homecare patients on the island of Oahu, in Hawaii. We are an in home care company called Brantley Homecare. Our care services are provided 24/7, so we need staff that can work days, nights, weekdays, weekends. We need catchy fun ads to entice caregivers and nurses to call our office to inquire about jobs available. Our patients age range is from babies to seniors. We need caregivers and nurses for basic patient care (bathing, dressing, ambulating, preparing meals, medication reminders, light housekeeping) and complex patients (oxygen, tube feeding, injections, vents, wound care). Here are some bullets to consider including:
*Full-time and Part-time Positions Available (days, nights, weekdays, weekends)
*Sign-On Bonus Programs Offered up to $500
*Refer a Friend Bonus Program
*Holiday Pay
*2 Health Plans to Choose from
*Island-Wide Locations
*All PPE Provided (masks, gloves, etc)
*401K Program
*Tuition Benefits

```html
<!DOCTYPE html>
<html lang="en">
<head>
<meta charset="UTF-8">
<title>Brantley Homecare – We are Recruiting</title>
<link href="https://fonts.googleapis.com/css2?family=Montserrat:wght@400;500;700;800;900&display=swap" rel="stylesheet">
<style>
  :root{
    --sky:#00aeef;
    --sky-soft:#bfe3f7;
    --sky-pale:#e6f4fc;
    --ink:#0b0b0b;
    --white:#ffffff;
    --backdrop:#e2e3e5;
  }
  *{margin:0;padding:0;box-sizing:border-box}
  html,body{width:1200px;height:928px;overflow:hidden;background:var(--backdrop);font-family:"Montserrat",sans-serif}
  .flyer{
    position:absolute;left:71px;top:64px;width:1059px;height:784px;
    background:linear-gradient(180deg,var(--white) 0%,var(--white) 45%,var(--sky-pale) 78%,var(--sky-soft) 100%);
    box-shadow:4px 6px 10px rgba(0,0,0,.18);overflow:hidden;
  }
  .header-band{position:absolute;left:0;top:0;width:1059px;height:230px}
  .brand{position:absolute;left:82px;top:58px;width:230px;text-align:center;color:var(--white);font-weight:700}
  .brand-mark{width:58px;height:58px;border-radius:8px;background:var(--white);margin:0 auto 16px}
  .brand-name{font-size:40px;line-height:1;letter-spacing:-.5px}
  .brand-sub{font-size:15px;letter-spacing:7px;margin-top:8px}
  .headline{position:absolute;left:320px;top:64px;font-weight:900;font-size:62px;letter-spacing:-1px;color:var(--ink);line-height:1}
  .headline .accent{color:var(--white)}
  .location{position:absolute;left:320px;top:135px;font-size:33px;font-weight:400;color:var(--white);line-height:1}
  .location .place{color:var(--ink)}
  .hero-photo{
    position:absolute;left:0;top:230px;width:485px;height:554px;
    background:radial-gradient(ellipse at 55% 55%,#4f8fd6 0%,#8cc0ea 40%,#d3ebfa 75%,rgba(255,255,255,0) 100%);
  }
  .benefits{position:absolute;left:436px;top:253px;list-style:none}
  .benefit{display:flex;align-items:center;height:40px;font-size:18.5px;font-weight:500;color:var(--ink);line-height:1.2}
  .benefit.tall{height:60px;margin-bottom:-6px}
  .benefit svg{width:32px;height:32px;flex:none;margin-right:17px;stroke:var(--sky);fill:none;stroke-width:2;stroke-linecap:round;stroke-linejoin:round}
  .phone-pill{
    position:absolute;left:514px;top:640px;width:438px;height:76px;border-radius:22px;
    background:var(--sky);color:var(--white);font-weight:800;font-size:44px;
    display:flex;align-items:center;justify-content:center;letter-spacing:.5px
  }
  .web{position:absolute;left:514px;width:438px;top:730px;text-align:center;font-size:31px;font-weight:500;color:var(--ink)}
</style>
</head>
<body>
<div class="flyer">
  <svg class="header-band" viewBox="0 0 1059 230" preserveAspectRatio="none">
    <path d="M0 0H1059V178C800 205 420 222 0 225Z" fill="var(--sky)"/>
  </svg>

  <div class="brand">
    <div class="brand-mark"></div>
    <div class="brand-name">Brantley</div>
    <div class="brand-sub">HOMECARE</div>
  </div>

  <h1 class="headline">We are <span class="accent">Recruiting</span></h1>
  <p class="location">Location : <span class="place">Oahu, Hawaii</span></p>

  <div class="hero-photo" role="img" aria-label="Smiling nurse in blue scrubs pointing to herself, with soft blue tropical leaves behind her"></div>

  <ul class="benefits">
    <li class="benefit tall">
      <svg viewBox="0 0 32 32"><circle cx="16" cy="9" r="5"/><path d="M5 29c0-7 5-12 11-12s11 5 11 12M16 17l-2 6 2 3 2-3z"/></svg>
      <span>Full-time and Part-time Positions Available<br>(days, nights, weekdays, weekends)</span>
    </li>
    <li class="benefit">
      <svg viewBox="0 0 32 32"><path d="M6 10V5h21v22H6v-5M3 16h15M13 11l5 5-5 5"/></svg>
      <span>Sign-On Bonus Programs Offered up to $500</span>
    </li>
    <li class="benefit">
      <svg viewBox="0 0 32 32"><path d="M28 14a12 12 0 1 1-4-8"/><path d="M24 3v4h4"/><circle cx="12" cy="13" r="1"/><circle cx="20" cy="13" r="1"/><path d="M10 19c3 4 9 4 12 0"/></svg>
      <span>Refer a Friend Bonus Program</span>
    </li>
    <li class="benefit">
      <svg viewBox="0 0 32 32"><circle cx="16" cy="16" r="13"/><path d="M20 11c-1-2-8-2-8 1.5s8 2.5 8 6.5-7 3.5-8 1M16 7v18"/></svg>
      <span>Holiday Pay</span>
    </li>
    <li class="benefit">
      <svg viewBox="0 0 32 32"><path d="M6 6l10 12 10-12M16 18v9M6 6v5M6 6h5M26 6v5M26 6h-5"/><circle cx="16" cy="26" r="2"/></svg>
      <span>2 Health Plans to Choose from</span>
    </li>
    <li class="benefit">
      <svg viewBox="0 0 32 32"><path d="M16 29s-9-9-9-16a9 9 0 0 1 18 0c0 7-9 16-9 16z"/><circle cx="16" cy="13" r="3"/></svg>
      <span>Island-Wide Locations</span>
    </li>
    <li class="benefit">
      <svg viewBox="0 0 32 32"><path d="M3 11c4 0 8-3 13-3s9 3 13 3c0 8-6 13-13 13S3 19 3 11zM16 12v7M12.5 15.5h7"/></svg>
      <span>All PPE Provided (masks, gloves, etc)</span>
    </li>
    <li class="benefit">
      <svg viewBox="0 0 32 32"><rect x="6" y="7" width="24" height="15" rx="1"/><path d="M3 10v15h23"/><circle cx="18" cy="14.5" r="3"/><path d="M10 14.5h2M24 14.5h2"/></svg>
      <span>401K Program</span>
    </li>
    <li class="benefit">
      <svg viewBox="0 0 32 32"><path d="M2 14l14-5 14 5-14 5zM8 16v5c4 3 12 3 16 0v-5M3 15v7"/></svg>
      <span>Tuition Benefits</span>
    </li>
  </ul>

  <div class="phone-pill">808-555-0142</div>
  <div class="web">www.brantleycare.com</div>
</div>
</body>
</html>
```